Etiqueta para productos de Panaderia Serenita

Necesitamos hacer una actualizacion de nuestra etiqueta con el slogan "Tibio del Horno", les adjunto foto de la etiqueta actual y fotos de los productos en los cuales utilizamos esta etiqueta.
Somos una empresa de panaderia, ubicados en Honduras
Distribuidora Trigal SA de CV

Target Market(s)

Clientes en Supermercados

Industry/Entity Type

Panaderia

```html
<!DOCTYPE html>
<html lang="es">
<head>
<meta charset="utf-8">
<title>Etiqueta Tibio del Horno — Panaderia Serenita</title>
<link rel="stylesheet" href="https://fonts.googleapis.com/css2?family=Bebas+Neue&family=Quicksand:wght@600;700&family=Montserrat:wght@400;600;700&display=swap">
<style>
  :root {
    --backdrop: #d8d0cb;
    --pink: #eba6a8;
    --cream: #f4eddc;
    --teal: #a8d4cf;
    --ink: #1f2328;
    --slate: #4c5a5e;
    --badge-ring: #5f6f73;
    --note-bg: #f6f4ee;
    --portrait-a: #f1e6d6;
    --portrait-b: #7fc0b8;
    --wheat: #e7decb;
  }
  * { margin: 0; padding: 0; box-sizing: border-box; }
  html, body { width: 1200px; height: 862px; overflow: hidden; }
  body { background: var(--backdrop); position: relative; font-family: "Montserrat", sans-serif; color: var(--ink); }

  .label {
    position: absolute; left: 295px; top: 50px; width: 610px; height: 762px;
    border-radius: 16px; overflow: hidden; background: var(--cream);
  }
  .band-top { position: absolute; left: 0; top: 0; width: 100%; height: 232px; background: var(--pink); }
  .band-bottom { position: absolute; left: 0; bottom: 0; width: 100%; height: 121px; background: var(--teal); }

  .portrait {
    position: absolute; left: 37px; top: 107px; width: 272px; height: 272px; border-radius: 50%;
    border: 6px solid var(--ink);
    background: radial-gradient(circle at 50% 38%, var(--portrait-a) 0 48%, var(--portrait-b) 75%);
  }

  .brand {
    position: absolute; left: 345px; top: 56px; display: flex; align-items: center; gap: 10px;
    font-family: "Montserrat", sans-serif; font-weight: 700; font-size: 30px; letter-spacing: 1px; color: var(--ink);
  }
  .brand-dot { width: 22px; height: 22px; border-radius: 50%; background: var(--ink); }

  .weight {
    position: absolute; left: 413px; top: 190px; width: 154px; height: 154px; border-radius: 50%;
    border: 3px solid var(--badge-ring); color: var(--slate); text-align: center;
    display: flex; flex-direction: column; align-items: center; justify-content: center;
  }
  .weight-caption { font-size: 11px; font-weight: 700; letter-spacing: 1px; }
  .weight-value {
    margin: 6px 0; width: 88px; height: 88px; border-radius: 50%; border: 3px solid var(--badge-ring);
    font-size: 40px; font-weight: 400; line-height: 82px;
  }

  .slogan-lead {
    position: absolute; left: 320px; top: 344px; width: 130px; text-align: right;
    font-family: "Quicksand", sans-serif; font-weight: 700; font-size: 40px; line-height: 42px; color: var(--ink);
  }
  .slogan-main {
    position: absolute; left: 36px; top: 444px; width: 418px; text-align: center;
    font-family: "Bebas Neue", sans-serif; font-size: 162px; line-height: 150px; letter-spacing: 14px; color: var(--ink);
  }
  .wheat { position: absolute; left: 468px; top: 340px; width: 96px; height: 280px; border-radius: 48px; background: var(--wheat); }

  .tagline {
    position: absolute; left: 36px; top: 598px; width: 418px; display: flex; align-items: center; gap: 10px;
    font-size: 15px; letter-spacing: 2.5px; color: var(--slate); white-space: nowrap;
  }
  .tagline::before, .tagline::after { content: ""; flex: 1; height: 2px; background: var(--slate); }

  .features { position: absolute; left: 0; top: 662px; width: 360px; display: flex; align-items: flex-start; }
  .feature { width: 120px; text-align: center; font-size: 8.5px; font-weight: 700; line-height: 11px; color: var(--slate); }
  .feature svg { display: block; margin: 0 auto 10px; }
  .divider { width: 2px; height: 42px; background: var(--slate); margin-top: 6px; }

  .ingredients {
    position: absolute; left: 366px; top: 660px; width: 204px; height: 88px; background: var(--note-bg);
    padding: 8px 10px; font-size: 8.5px; line-height: 12px; color: var(--slate);
  }
  .ingredients strong { display: block; font-size: 11px; color: var(--ink); margin-bottom: 3px; }
</style>
</head>
<body>
  <section class="label">
    <div class="band-top"></div>
    <div class="band-bottom"></div>

    <div class="portrait" role="img" aria-label="Ilustración de una abuela sonriente con moño blanco y collar de perlas"></div>

    <div class="brand"><span class="brand-dot"></span>HORNOVA</div>

    <div class="weight">
      <span class="weight-caption">PESO NETO</span>
      <span class="weight-value">320</span>
      <span class="weight-caption">GRAMOS</span>
    </div>

    <p class="slogan-lead">TIBIO<br>DEL</p>
    <h1 class="slogan-main">HORNO</h1>
    <div class="wheat" role="img" aria-label="Ilustración de una espiga de trigo"></div>

    <p class="tagline">LOS MEJORES INGGREDIENTES</p>

    <div class="features">
      <div class="feature">
        <svg width="34" height="36" viewBox="0 0 34 36" fill="none" stroke="#4c5a5e" stroke-width="3">
          <path d="M5 6h16v26H5z"/><circle cx="25" cy="26" r="6"/><path d="M13 14v8M9 18h8"/>
        </svg>
        LOS MEJORES<br>INGREDIENTES
      </div>
      <div class="divider"></div>
      <div class="feature">
        <svg width="40" height="36" viewBox="0 0 40 36">
          <path d="M4 24c0-9 7-14 16-14s16 5 16 14v3H4z" fill="#4c5a5e"/>
        </svg>
        PAN<br>ARTESENAL
      </div>
      <div class="divider"></div>
      <div class="feature">
        <svg width="36" height="36" viewBox="0 0 36 36" fill="none" stroke="#4c5a5e" stroke-width="3" stroke-linecap="round">
          <path d="M18 3v30M5 10.5l26 15M5 25.5l26-15"/>
          <path d="M14 5l4 4 4-4M14 31l4-4 4 4"/>
        </svg>
        RECOMENDAMOS<br>REFRIGERAR
      </div>
    </div>

    <div class="ingredients">
      <strong>Ingredientes:</strong>
      Agua, sal, margarina, azúcar, esencia de vainilla, preservantes y polvo de hornear. Contiene huevos, leche en polvo y trigo.
    </div>
  </section>
</body>
</html>
```